Brightmerepathways.com is URL - need full website design

We need a website design created for our new business, Brightmere Pathways International. Our services include mastermind groups, speaking & workshops, life coaching, leadership assessment and spiritual enrichment. Our design colors are purple, gold and white. Our final web design should reflect and communicate positive growth, learning and professional development in all endeavors. Our budget is $618.00. Need 8 pages on website.
Churches, mid to large organizations, schools, universities, and individuals
Brightmere Pathways International
Must have
- email accounts
- A Page to place orders
- Need to add to FB, Chirper, Livescope, ClipCam, and Callwave
- Logo Design:
- Need only 1 globe. Base color : purple. Continents color: gold & lines color: white
- Would like a hand holding the globe
- Sunshine rays over top - either white or gold
- Name: "Brightmere Pathways" in center of globe & "International" at bottom of globe sort of rounded.

```html
<!DOCTYPE html>
<html lang="en">
<head>
<meta charset="utf-8">
<title>Our Services – Brightmere Pathways International</title>
<link rel="stylesheet" href="https://fonts.googleapis.com/css2?family=Open+Sans:wght@400;600&family=Roboto:wght@400;500&family=Roboto+Condensed:wght@500;700&display=swap">
<style>
:root{
  --orange:#e8861f;
  --orange-footer:#e98a20;
  --ink:#2b2b2b;
  --text:#555;
  --frame:#e6e6e6;
  --bar:#222;
  --white:#fff;
}
*{box-sizing:border-box;margin:0;padding:0}
html,body{width:1200px;height:2490px;overflow:hidden}
body{position:relative;background:var(--white);font-family:"Open Sans",sans-serif;color:var(--text)}

.site-header{position:absolute;top:0;left:0;width:1200px;height:96px;background:var(--white)}
.brand{position:absolute;left:100px;top:30px;display:flex;align-items:center;gap:10px}
.brand-name{font-family:"Open Sans",sans-serif;font-weight:600;font-size:21px;color:#2d3a4a;letter-spacing:.5px;text-transform:uppercase}
.brand-dot{width:30px;height:30px;border-radius:50%;border:3px solid var(--orange)}
.main-nav{position:absolute;right:100px;top:0;height:96px;display:flex}
.main-nav a{display:flex;align-items:center;padding:0 20px;font-family:"Roboto",sans-serif;font-size:13px;color:#333;text-decoration:none;text-transform:uppercase}
.main-nav a.active{background:var(--orange);color:var(--white)}

.page-hero{position:absolute;top:96px;left:0;width:1200px;height:213px;
  background:radial-gradient(ellipse at 60% 30%,#b9c8d6 0%,#6f8aa6 30%,#2e4563 65%,#1a2838 100%);display:flex;align-items:center;justify-content:center}
.page-hero h1{font-family:"Roboto Condensed",sans-serif;font-weight:700;font-size:44px;color:var(--white);letter-spacing:.5px}

.photo{position:absolute;border:5px solid var(--frame)}
.service{position:absolute;width:469px}
.service-head{display:flex;align-items:center;gap:20px;margin-bottom:20px}
.service-icon{width:58px;height:58px;border-radius:50%;background:var(--orange);flex:none;display:flex;align-items:center;justify-content:center}
.service-title{font-family:"Roboto",sans-serif;font-size:20px;color:var(--ink);line-height:1.15;text-transform:uppercase}
.service-sub{font-family:"Open Sans",sans-serif;font-size:15px;color:#555;text-transform:none;margin-top:2px}
.service p{font-size:11.5px;line-height:24px;color:#555;margin-bottom:4px;text-align:justify}
.bullets{list-style:none;margin:6px 0 8px}
.bullets li{position:relative;padding-left:26px;font-size:11.5px;line-height:25.5px;color:#555}
.bullets li::before{content:"";position:absolute;left:0;top:7px;width:11px;height:11px;border-radius:50%;background:#333}
.bullets li::after{content:"";position:absolute;left:3px;top:10px;width:3px;height:3px;border-right:1.5px solid #fff;border-top:1.5px solid #fff;transform:rotate(45deg)}
.levels{font-size:14px;color:#444;margin:6px 0 2px 4px}
.service-continued{position:absolute;left:100px;top:2022px;width:1000px;font-size:11.5px;line-height:24px;color:#555}

.site-footer{position:absolute;top:2170px;left:0;width:1200px;height:262px;background:var(--orange-footer);color:var(--white)}
.footer-col{position:absolute;top:40px}
.footer-col h3{font-family:"Open Sans",sans-serif;font-weight:600;font-size:15px;text-transform:uppercase;margin-bottom:22px}
.contact-row{display:flex;gap:18px;font-size:12.5px;line-height:20px;margin-bottom:16px}
.contact-row svg{flex:none;margin-top:2px}
.signup p{font-size:11px;line-height:19px;width:300px;margin-bottom:14px}
.field{width:325px;height:41px;background:var(--white);color:#333;font-size:11px;padding:13px 14px;margin-bottom:10px;position:relative}
.subscribe{position:absolute;right:4px;top:4px;height:33px;width:97px;background:var(--bar);color:var(--white);font-size:12px;display:flex;align-items:center;justify-content:center;text-transform:uppercase}
.social-grid{display:grid;grid-template-columns:148px 120px;row-gap:14px}
.social-grid span{display:flex;align-items:center;gap:10px;font-size:13px}
.social-grid i{width:24px;height:24px;border:1.5px solid var(--white);border-radius:50%}
.copyright{position:absolute;top:2432px;left:0;width:1200px;height:58px;background:var(--bar);color:#ddd;font-size:12px;display:flex;align-items:center;justify-content:center}
</style>
</head>
<body>

<header class="site-header">
  <div class="brand"><span class="brand-name">Brightmere Pathways</span><span class="brand-dot"></span></div>
  <nav class="main-nav">
    <a href="#">Home</a><a href="#">About Us</a><a href="#" class="active">Our Services</a><a href="#">News</a><a href="#">Contact Us</a>
  </nav>
</header>

<section class="page-hero" role="img" aria-label="Open book beneath a bright cloudy sky"><h1>OUR SERVICES</h1></section>

<div class="photo" role="img" aria-label="Hands folded in prayer" style="left:100px;top:363px;width:498px;height:351px;background:linear-gradient(135deg,#9bbfc6,#d9b8a6 55%,#7d7a72)"></div>
<article class="service" style="left:631px;top:365px">
  <div class="service-head">
    <div class="service-icon"><svg width="30" height="30" viewBox="0 0 30 30"><circle cx="15" cy="15" r="11" fill="none" stroke="#fff" stroke-width="3"/><circle cx="15" cy="15" r="5" fill="none" stroke="#fff" stroke-width="3"/></svg></div>
    <h2 class="service-title">Spiritual Guidance<br>and Enrichment</h2>
  </div>
  <p>We offer spiritual guidance and enrichment resources by utilizing biblically sound principals, that can be applied to one's practical lifestyle, and to help you navigate through the journey of life. This program includes several lessons on the following subjects and many more. To name a few are:</p>
  <ul class="bullets">
    <li>Forgiveness &amp; Healing</li><li>Anger Management</li><li>Stress Management</li><li>Grief &amp; Loss</li><li>Relationships</li><li>Marriage</li><li>Conflict Resolution</li>
  </ul>
</article>

<article class="service" style="left:100px;top:795px">
  <div class="service-head">
    <div class="service-icon"><svg width="30" height="30" viewBox="0 0 30 30"><rect x="6" y="6" width="16" height="18" fill="none" stroke="#fff" stroke-width="2.5"/><path d="M12 20 L24 8" stroke="#fff" stroke-width="3"/></svg></div>
    <h2 class="service-title">Mastermind Groups<div class="service-sub">Nemo enim ipsam voluptatem quia voluptas sit</div></h2>
  </div>
  <p>Mastermind groups bring together highly motivated like-minded individuals, as well as provide an environment for brainstorming, which adds value along with support in a group setting. It garners excitement, commitment, and accountability, while sharpening the mind and skills of each participant, by combining fresh ideas, different perspectives and educational synergy. The benefits of a Mastermind group includes the following:</p>
  <ul class="bullets">
    <li>Increase self confidence and positive mental demeanor</li><li>Gain knowledge and understanding of growth and leadership principals</li><li>Encourages business and personal development</li><li>Optimism and accountability support</li>
  </ul>
  <p>Brightmere Pathways International, through Masterminds, can help you or your organization achieve success.</p>
</article>
<div class="photo" role="img" aria-label="Business team meeting around a table in a bright office" style="left:601px;top:792px;width:499px;height:350px;background:linear-gradient(160deg,#f1f4f7,#cfd6dd 50%,#6b6f78)"></div>

<div class="photo" role="img" aria-label="Speaker in a suit addressing a seated audience" style="left:100px;top:1223px;width:498px;height:346px;background:linear-gradient(100deg,#b9a59a,#d98566 40%,#2c3b5a 75%,#1d2a44)"></div>
<article class="service" style="left:631px;top:1220px">
  <div class="service-head">
    <div class="service-icon"><svg width="30" height="30" viewBox="0 0 30 30"><path d="M7 23 C7 12 14 7 24 6 C23 16 18 23 7 23 Z" fill="#fff"/><path d="M7 23 L17 13" stroke="#e8861f" stroke-width="2"/></svg></div>
    <h2 class="service-title">Coaching Services</h2>
  </div>
  <p>As your Certified Harlan Whitcombe life coach. We will make it my priority to understand you, what's important to you, and the specific area(s) in your life that you need guidance with. We will diligently work along side you, to stretch and grow you into gaining the right insight while simultaneously empowering you. Our focus here will be all about you. You will be in the position to overcome barriers in your pathway, while helping you attain and aspire to your life goals.</p>
  <div class="levels">We offer two levels of coaching:</div>
  <ul class="bullets">
    <li>Individual Coaching – One on one private and confidential coaching</li><li>Group Coaching – small setting onsite or via webinar, conference</li>
  </ul>
  <p>Please contact us and together we'll create the most effective plan to move you forward in the right direction.</p>
</article>

<article class="service" style="left:100px;top:1643px">
  <div class="service-head">
    <div class="service-icon"><svg width="30" height="30" viewBox="0 0 30 30"><circle cx="15" cy="11" r="5" fill="#fff"/><path d="M5 25 C6 18 24 18 25 25 Z" fill="#fff"/></svg></div>
    <h2 class="service-title">Speaking Workshops<br>Seminars &amp; Leadership Assessment:</h2>
  </div>
  <p>As a Certified Harlan Whitcombe Coach, Trainer and Speaker, we offer customized presentations to fit your individual or team's needs and budget such as:</p>
  <ul class="bullets">
    <li>Keynote speech for your company sponsored event</li><li>Half day and full day workshop/seminar</li><li>In-house corporate training</li><li>Executive and personal retreat</li><li>Leadership Assessment</li>
  </ul>
  <p>We will provide effective team communication and structure that is important for forging relationships equipping your team with the proper attitudes to develop leaders within. We will assess your team to determine what would be the best course of action, and present the necessary leadership program materials needed. We will work</p>
</article>
<div class="photo" role="img" aria-label="Presenter with microphone and tablet in front of a conference audience" style="left:601px;top:1643px;width:499px;height:346px;background:linear-gradient(120deg,#c9b9a8,#e8ddd2 45%,#8aa2c4 70%,#3a3a3a)"></div>
<p class="service-continued">through goal setting and communication exercises that will bring cohesiveness to your group ultimately increasing productivity due to the positive influences each member will have on the group as a whole. In addition, we will at your request, incorporate your organization's meeting theme, mission / vision statement or build on your existing training schedule to best fit the needs of your group. Please contact Brightmere Pathways International for more information.</p>

<footer class="site-footer">
  <div class="footer-col" style="left:98px">
    <h3>Contact Us</h3>
    <div class="contact-row"><svg width="16" height="20" viewBox="0 0 16 20"><path d="M8 1 C4 1 1.5 4 1.5 7.5 C1.5 12 8 19 8 19 C8 19 14.5 12 14.5 7.5 C14.5 4 12 1 8 1 Z" fill="none" stroke="#fff" stroke-width="1.5"/><circle cx="8" cy="7.5" r="2.3" fill="none" stroke="#fff" stroke-width="1.5"/></svg><div>Brightmere Pathways International<br>P.O. Box 4820 Lakeridge,<br>TX 75390 555-014-2290</div></div>
    <div class="contact-row"><svg width="18" height="18" viewBox="0 0 18 18"><path d="M4 1 L7 5 L5 7 C6 10 8 12 11 13 L13 11 L17 14 L15 17 C8 16 2 10 1 3 Z" fill="none" stroke="#fff" stroke-width="1.5"/></svg><div>+555-014-2290</div></div>
    <div class="contact-row"><svg width="20" height="14" viewBox="0 0 20 14"><rect x="1" y="1" width="18" height="12" fill="none" stroke="#fff" stroke-width="1.5"/><path d="M1 1 L10 8 L19 1" fill="none" stroke="#fff" stroke-width="1.5"/></svg><div>hello@brightmerepathways.com</div></div>
  </div>
  <div class="footer-col signup" style="left:420px">
    <h3>Sign Up to Receive Email</h3>
    <p>Excepteur sint occaecat cupidatat non proident, sunt in culpa qui Nemo enim ipsam voluptatem</p>
    <div class="field">Enter Name</div>
    <div class="field">Enter Email<span class="subscribe">Subscribe</span></div>
  </div>
  <div class="footer-col" style="left:847px">
    <h3>Social Networks</h3>
    <div class="social-grid">
      <span><i></i>Faceline</span><span><i></i>ClipCam</span>
      <span><i></i>Chirper</span><span><i></i>Callwave</span>
      <span><i></i>Livescope</span>
    </div>
  </div>
</footer>
<div class="copyright">Copyright © Brightmere Pathways International 2016. All rights reserved.</div>

</body>
</html>
```